Kestrel Electrical Business Card

We need a business card design for our family-run electrical contracting business based in Western Australia called 'Kestrel Electrical'. We provide electrical services including residential, commercial and industrial. We aim for individual business cards to be made for all of our employees. We already have a company logo, which we require to be featured on the design. We would like simple, sleek and vibrant designs, which incorporate our logo and represent our business. We do not want anything involving too many graphics/images. We like the colours red, black, white and all shades of grey. The final design should communicate professionalism and trustworthiness.
We require the following contact information:
Name- Owen Strickland
EC 5809
Mobile number- 0455 918 302
Fax number (including area code)- (08) 9640 2718
Email adress- name@kestrelelectrical.example
Electrical
- ITC Handel Bold

```html
<!DOCTYPE html>
<html lang="en">
<head>
<meta charset="UTF-8">
<title>Kestrel Electrical – Business Card</title>
<link rel="stylesheet" href="https://fonts.googleapis.com/css2?family=Russo+One&display=swap">
<style>
  :root {
    --red: #e3202a;
    --red-deep: #a50d16;
    --red-glow: #ec2532;
    --white: #ffffff;
    --black: #141414;
    --grey: #8a8a8a;
    --card-w: 1200px;
    --card-h: 741px;
  }
  * { margin: 0; padding: 0; box-sizing: border-box; }
  html, body {
    width: var(--card-w);
    height: var(--card-h);
    overflow: hidden;
    background: var(--white);
  }
  .card {
    position: relative;
    width: var(--card-w);
    height: var(--card-h);
    overflow: hidden;
    font-family: "Russo One", sans-serif;
    background: radial-gradient(ellipse 70% 75% at 48% 48%, var(--red-glow) 0%, var(--red) 35%, var(--red-deep) 100%);
  }
  .identity-band {
    position: absolute;
    left: 0; top: 128px;
    width: 100%; height: 126px;
    background: var(--white);
  }
  .brand {
    position: absolute;
    left: 92px; top: 170px;
    display: flex;
    align-items: center;
    gap: 18px;
  }
  .brand-mark {
    width: 62px; height: 62px;
    background: var(--red);
  }
  .brand-name {
    color: var(--black);
    font-size: 40px;
    line-height: 1;
    letter-spacing: 1px;
    text-transform: uppercase;
  }
  .person {
    position: absolute;
    right: 80px; top: 145px;
    text-align: right;
  }
  .person-name {
    font-size: 56px;
    line-height: 1;
    color: var(--black);
    white-space: nowrap;
  }
  .person-name .first { color: var(--red); }
  .licence {
    margin-top: 6px;
    font-size: 42px;
    line-height: 1;
    color: var(--grey);
    letter-spacing: 1px;
  }
  .contact {
    position: absolute;
    right: 80px; top: 372px;
    text-align: right;
    color: var(--white);
    list-style: none;
    white-space: nowrap;
  }
  .contact li { line-height: 1; }
  .contact .mobile { font-size: 42px; margin-bottom: 14px; }
  .contact .fax { font-size: 32px; margin-bottom: 20px; }
  .contact .email { font-size: 30px; }
  .services-tab {
    position: absolute;
    left: 90px; top: 612px;
    width: 1200px; height: 200px;
    background: var(--white);
    border-radius: 110px 110px 0 0;
  }
  .services {
    position: absolute;
    left: 0; top: 640px;
    width: 1242px;
    text-align: center;
    color: var(--red);
    font-size: 37px;
    line-height: 1;
    white-space: nowrap;
  }
  .services .divider {
    color: var(--grey);
    margin: 0 14px;
    font-size: 30px;
  }
</style>
</head>
<body>
  <div class="card">
    <div class="identity-band"></div>

    <div class="brand">
      <span class="brand-mark"></span>
      <span class="brand-name">Kestrel Electrical</span>
    </div>

    <div class="person">
      <div class="person-name"><span class="first">Owen</span> Strickland</div>
      <div class="licence">EC 5809</div>
    </div>

    <ul class="contact">
      <li class="mobile">M: 0455 918 302</li>
      <li class="fax">F: (08) 9640 2718</li>
      <li class="email">E: NAME@KESTRELELECTRICAL.EXAMPLE</li>
    </ul>

    <div class="services-tab"></div>
    <div class="services">
      RESIDENTIAL<span class="divider">|</span>COMMERCIAL<span class="divider">|</span>INDUSTRIAL
    </div>
  </div>
</body>
</html>
```